Design few pages for professional development app

I need a website design for a prototype project. The goal of the project is to prototype a few basic screens for a professional development application.

The final design should be clean, modern, and appeal to a professional millenial clientele.The designs have been wireframed (see attached), and we'd like these wireframes converted to design files.

Here is the list of goals and tasks that correspond to the design: https://sheets.plorvane.com/grid/d/7kQWm48p3XZvrt2bYH5LcNaeJoTsUDfi82GhKxMp/edit?view=shared

Number of Pages Required

5+ page

Font styles to use
Serif
Sans Serif

Colors

Designer to choose colors to be used in the design.

Requirements
Nice to have
• Uses Google Material Design, Bootstrap, or another framework

```html
<!DOCTYPE html>
<html lang="en">
<head>
<meta charset="utf-8">
<title>StrideUp – Career Growth Screens</title>
<link rel="stylesheet" href="https://fonts.googleapis.com/css2?family=Mulish:ital,wght@0,400;0,600;0,700;0,800;1,600&display=swap">
<style>
:root{
  --panel:#6481c0;
  --paper:#f2f5fb;
  --white:#ffffff;
  --ink:#1d1d1f;
  --muted:#8a8d93;
  --rose:#c55d87;
  --lime:#a6e47c;
  --check:#1e88e5;
  --gap:#9a9a9a;
  --line:#dfe4ee;
}
*{box-sizing:border-box;margin:0;padding:0}
html,body{width:1200px;height:2962px;overflow:hidden}
body{font-family:"Mulish",sans-serif;color:var(--ink);background:var(--paper)}
.screen{position:absolute;left:0;width:1200px;height:675px;background:var(--paper);overflow:hidden}
.band{position:absolute;left:0;width:1200px;height:87px;background:var(--gap)}
.side{position:absolute;left:0;top:0;height:675px;width:422px;background:var(--panel);color:var(--white)}
.side.wide{width:600px}
.side::after{content:"";position:absolute;right:-14px;top:321px;border-top:16px solid transparent;border-bottom:16px solid transparent;border-left:14px solid var(--panel)}
.brand{position:absolute;left:20px;top:12px;font-weight:800;font-size:14px;letter-spacing:.2px}
.search{position:absolute;top:12px;width:14px;height:14px}
.user{position:absolute;left:319px;top:13px;font-size:10px;font-weight:600;display:flex;align-items:center;gap:8px}
.user::after{content:"";border-left:4px solid transparent;border-right:4px solid transparent;border-top:5px solid var(--white)}
.center{position:absolute;left:0;width:100%;text-align:center}
.link-lime{color:var(--lime);font-weight:600;font-size:13px;border-bottom:2px solid var(--lime);padding-bottom:2px;text-decoration:none}
.btn{position:absolute;display:flex;align-items:center;justify-content:center;font-weight:800;font-size:13px;color:var(--white);background:var(--rose);text-decoration:none}
.btn.lime{background:var(--lime)}
.btn.ghost{background:transparent;border:2px solid var(--lime);color:var(--lime);font-weight:600}
/* sign up */
.hero-title{top:290px;font-size:26px;font-weight:800;letter-spacing:.2px}
.hero-sub{top:337px;font-size:14.5px;font-weight:700;line-height:21px;padding:0 38px}
.quote{position:absolute;left:84px;top:604px;width:432px;height:50px;display:flex;align-items:center;gap:8px}
.arrow{width:10px;height:22px}
.avatar{width:48px;height:48px;border-radius:50%;background:radial-gradient(circle at 50% 40%,#e8c7b0,#8b5a3c);flex:none;margin-left:12px}
.quote p{font-size:12.5px;font-style:italic;font-weight:600;flex:1}
.quote small{display:block;font-size:10px;font-style:normal;margin-top:3px}
.signup-title{position:absolute;left:600px;width:600px;top:78px;text-align:center;font-size:18px;font-weight:400;color:#333}
.card{position:absolute;background:var(--white);border-radius:10px}
.field-label{position:absolute;left:42px;font-size:9.5px;font-weight:800}
.field{position:absolute;left:42px;height:42px;border:1px solid #222;background:var(--white)}
.help{position:absolute;left:299px;top:222px;width:22px;height:22px;border:1.5px solid #bbb;border-radius:50%;color:#aaa;font-size:13px;display:flex;align-items:center;justify-content:center}
.agree{position:absolute;left:42px;top:350px;display:flex;align-items:center;gap:10px;font-size:12.5px;color:#333}
.box{width:17px;height:17px;border:1.5px solid #555;background:var(--white)}
.agree a{color:var(--rose);text-decoration:none}
/* goals */
.goal{position:absolute;width:337px;height:245px;background:var(--white);border:1px solid transparent}
.goal.on{border-color:var(--check)}
.goal .tick{position:absolute;right:13px;top:13px;width:21px;height:21px;border:1.5px solid #777;display:flex;align-items:center;justify-content:center}
.goal.on .tick{background:var(--check);border-color:var(--check)}
.goal svg.icon{position:absolute;left:138px;top:73px;width:62px;height:62px}
.goal h3{position:absolute;top:163px;width:100%;text-align:center;font-size:14px;font-weight:800;letter-spacing:.3px}
.side h2{font-size:18px;font-weight:700}
.side .note{font-size:12.5px;margin-top:10px}
/* tasks */
.tasks{position:absolute;left:464px;top:43px;width:693px;display:flex;flex-direction:column;gap:11px}
.task{position:relative;height:66px;background:var(--white);border-radius:4px;display:flex;align-items:center;padding-left:20px}
.task.done{background:var(--paper);border:1px solid var(--line)}
.task svg.icon{width:26px;height:26px;flex:none;color:#333}
.task.done svg.icon{color:#aaa}
.task .txt{margin-left:16px}
.task h4{font-size:14px;font-weight:800;letter-spacing:.2px}
.task h4 span{font-size:9px;font-weight:600;color:var(--muted);margin-left:4px}
.task p{font-size:12.5px;color:#333;margin-top:1px}
.task.done h4,.task.done p{color:var(--muted)}
.task .act{position:absolute;right:20px;top:19px;width:28px;height:28px}
.tip{position:absolute;right:2px;top:-18px;background:#555;color:var(--white);font-size:9px;font-weight:700;padding:4px 11px;border-radius:2px}
.ring{position:absolute;left:122px;top:270px;width:178px;height:178px}
/* lesson */
.video{position:absolute;left:464px;top:43px;width:693px;height:402px;background:var(--white);border-radius:10px}
.shot{position:absolute;left:14px;top:14px;width:665px;height:374px;background:linear-gradient(135deg,#3a5a3d 0%,#7f8f86 35%,#c9c5b8 60%,#8a7a55 100%)}
.play{position:absolute;left:300px;top:155px;width:68px;height:68px}
.body-copy{position:absolute;left:464px;top:470px;width:693px;font-size:12.8px;line-height:21px;color:#333}
.body-copy ul{list-style:none;margin-top:21px}
.body-copy li::before{content:"+ ";margin-right:4px}
</style>
</head>
<body>
<svg width="0" height="0" style="position:absolute">
  <defs>
    <symbol id="i-globe" viewBox="0 0 64 64"><g fill="none" stroke="currentColor" stroke-width="2"><circle cx="32" cy="32" r="29"/><ellipse cx="32" cy="32" rx="13" ry="29"/><line x1="32" y1="3" x2="32" y2="61"/><line x1="3" y1="32" x2="61" y2="32"/><path d="M8 17h48M8 47h48"/></g></symbol>
    <symbol id="i-user" viewBox="0 0 64 64"><g fill="none" stroke="currentColor" stroke-width="2"><circle cx="32" cy="20" r="14"/><path d="M6 60v-6c0-10 9-17 20-17h12c11 0 20 7 20 17v6z"/></g></symbol>
    <symbol id="i-award" viewBox="0 0 64 64"><g fill="none" stroke="currentColor" stroke-width="2" stroke-linejoin="round"><path d="M32 3l6 5 8-1 3 7 7 4-1 8 4 6-4 6 1 8-7 4-3 7-8-1-6 5-6-5-8 1-3-7-7-4 1-8-4-6 4-6-1-8 7-4 3-7 8 1z"/><circle cx="32" cy="28" r="9"/><path d="M18 50l-7 12 9-3 4 6 7-12M46 50l7 12-9-3-4 6-7-12"/></g></symbol>
    <symbol id="i-bolt" viewBox="0 0 64 64"><path d="M38 3L14 36h16l-6 25 26-35H34z" fill="none" stroke="currentColor" stroke-width="2" stroke-linejoin="round"/></symbol>
    <symbol id="i-search" viewBox="0 0 16 16"><g fill="none" stroke="currentColor" stroke-width="2"><circle cx="7" cy="7" r="5"/><line x1="11" y1="11" x2="15" y2="15"/></g></symbol>
    <symbol id="i-play" viewBox="0 0 28 28"><circle cx="14" cy="14" r="14" fill="currentColor"/><path d="M11 8.5l8 5.5-8 5.5z" fill="#fff"/></symbol>
    <symbol id="i-done" viewBox="0 0 28 28"><circle cx="14" cy="14" r="12.5" fill="none" stroke="currentColor" stroke-width="2"/><path d="M8.5 14.5l4 4 7-8" fill="none" stroke="currentColor" stroke-width="2"/></symbol>
    <symbol id="i-tick" viewBox="0 0 16 16"><path d="M3 8l3.5 3.5L13 5" fill="none" stroke="#fff" stroke-width="2.2"/></symbol>
  </defs>
</svg>

<!-- Sign up -->
<section class="screen" style="top:0">
  <div class="side wide">
    <div class="brand">StrideUp</div>
    <svg class="search" style="left:566px;color:#fff"><use href="#i-search"/></svg>
    <h1 class="center hero-title">TAKE CONTROL OF YOUR CAREER</h1>
    <p class="center hero-sub">Complete short, actionable tasks guaranteed to get you further in your career, faster than ever. Ready to get started?</p>
    <div class="center" style="top:400px"><a class="link-lime" href="#">&gt;&nbsp; Learn More</a></div>
    <div class="quote">
      <svg class="arrow" viewBox="0 0 10 22"><path d="M9 1L1 11l8 10" fill="none" stroke="#fff" stroke-width="1.5"/></svg>
      <div class="avatar" role="img" aria-label="Portrait photo of the reviewer"></div>
      <p>I love how quickly I can do the tasks, and see progress.<small>- Lena Ortiz</small></p>
      <svg class="arrow" viewBox="0 0 10 22"><path d="M1 1l8 10-8 10" fill="none" stroke="#fff" stroke-width="1.5"/></svg>
    </div>
  </div>
  <h2 class="signup-title">Sign Up To See &amp; Save Your Goals</h2>
  <form class="card" style="left:642px;top:120px;width:515px;height:474px">
    <label class="field-label" style="top:41px">NAME</label><div class="field" style="top:56px;width:432px"></div>
    <label class="field-label" style="top:118px">EMAIL</label><div class="field" style="top:133px;width:432px"></div>
    <label class="field-label" style="top:195px">PASSWORD</label><div class="field" style="top:210px;width:246px"></div>
    <div class="help">?</div>
    <label class="field-label" style="top:272px">RE-TYPE PASSWORD</label><div class="field" style="top:287px;width:246px"></div>
    <div class="agree"><span class="box"></span><span>I agree to the <a href="#">Terms of Use</a> and <a href="#">Privacy Policy</a>.</span></div>
    <a class="btn" href="#" style="left:42px;top:391px;width:147px;height:41px">&gt;&nbsp; Sign Up</a>
  </form>
</section>
<div class="band" style="top:675px"></div>

<!-- Goals -->
<section class="screen" style="top:762px">
  <div class="side">
    <div class="brand">StrideUp</div>
    <svg class="search" style="left:286px;color:#fff"><use href="#i-search"/></svg>
    <div class="user">Nora Whitfield</div>
    <div class="center" style="top:335px"><h2>Nora, what are your main goals?</h2><p class="note">Tell us what you'd like to achieve with StrideUp.</p></div>
  </div>
  <div class="goal on" style="left:464px;top:54px"><span class="tick"><svg width="14" height="14"><use href="#i-tick"/></svg></span><svg class="icon"><use href="#i-globe"/></svg><h3>BUILD MY NETWORK</h3></div>
  <div class="goal on" style="left:822px;top:54px"><span class="tick"><svg width="14" height="14"><use href="#i-tick"/></svg></span><svg class="icon"><use href="#i-user"/></svg><h3>PERSONAL GROWTH</h3></div>
  <div class="goal on" style="left:464px;top:321px"><span class="tick"><svg width="14" height="14"><use href="#i-tick"/></svg></span><svg class="icon"><use href="#i-award"/></svg><h3>GET A PROMOTION</h3></div>
  <div class="goal" style="left:822px;top:321px"><span class="tick"></span><svg class="icon"><use href="#i-bolt"/></svg><h3>BE A BETTER LEADER</h3></div>
  <a class="btn" href="#" style="left:686px;top:587px;width:249px;height:41px">&gt;&nbsp; See My Personalized List</a>
</section>
<div class="band" style="top:1437px"></div>

<!-- Task list -->
<section class="screen" style="top:1524px">
  <div class="side">
    <div class="brand">StrideUp</div>
    <svg class="search" style="left:286px;color:#fff"><use href="#i-search"/></svg>
    <div class="user">Nora Whitfield</div>
    <h2 class="center" style="top:220px">Nora, here's your list of suggested tasks.</h2>
    <svg class="ring" viewBox="0 0 178 178">
      <circle cx="89" cy="89" r="84" fill="none" stroke="#a7a7a9" stroke-width="6"/>
      <path d="M89 5A84 84 0 0 1 148 29" fill="none" stroke="var(--lime)" stroke-width="6"/>
      <text x="90" y="96" text-anchor="end" font-family="Mulish,sans-serif" font-size="50" fill="#fff">2</text>
      <text x="94" y="96" font-family="Mulish,sans-serif" font-size="17" fill="#fff">/16</text>
      <text x="89" y="118" text-anchor="middle" font-family="Mulish,sans-serif" font-size="9.5" font-weight="800" fill="#fff">COMPLETED</text>
    </svg>
    <div class="center" style="top:470px;left:-2px"><a class="link-lime" href="#">&gt;&nbsp; Re-personalize the List</a></div>
  </div>
  <div class="tasks">
    <div class="task done"><svg class="icon"><use href="#i-user"/></svg><div class="txt"><h4>PERSONAL GROWTH<span>(30 min.)</span></h4><p>Write your personal brand statement</p></div><svg class="act" style="color:var(--check)"><use href="#i-done"/></svg></div>
    <div class="task done"><svg class="icon"><use href="#i-award"/></svg><div class="txt"><h4>GET A PROMOTION<span>(60 min.)</span></h4><p>Have a career conversation with your manager</p></div><svg class="act" style="color:var(--check)"><use href="#i-done"/></svg></div>
    <div class="task"><svg class="icon"><use href="#i-award"/></svg><div class="txt"><h4>GET A PROMOTION<span>(60 min.)</span></h4><p>Ask for peer feedback</p></div><span class="tip">Start Task</span><svg class="act" style="color:var(--check)"><use href="#i-play"/></svg></div>
    <div class="task"><svg class="icon"><use href="#i-globe"/></svg><div class="txt"><h4>BUILD MY NETWORK<span>(30 min.)</span></h4><p>Make a list of influential people in your field at your company, and outside of your company</p></div><svg class="act" style="color:var(--rose)"><use href="#i-play"/></svg></div>
    <div class="task"><svg class="icon"><use href="#i-bolt"/></svg><div class="txt"><h4>BE A BETTER LEADER</h4><p>Have a career conversation with your direct report</p></div><svg class="act" style="color:var(--rose)"><use href="#i-play"/></svg></div>
    <div class="task"><svg class="icon"><use href="#i-bolt"/></svg><div class="txt"><h4>BE A BETTER LEADER</h4><p>Solicit feedback from your direct reports</p></div><svg class="act" style="color:var(--rose)"><use href="#i-play"/></svg></div>
    <div class="task"><svg class="icon"><use href="#i-bolt"/></svg><div class="txt"><h4>BE A BETTER LEADER</h4><p>Meet with your skip-level reports</p></div><svg class="act" style="color:var(--rose)"><use href="#i-play"/></svg></div>
    <div class="task"><svg class="icon"><use href="#i-award"/></svg><div class="txt"><h4>GET A PROMOTION</h4><p>Set up a career lunch with someone at a higher level besides your manager</p></div><svg class="act" style="color:var(--rose)"><use href="#i-play"/></svg></div>
    <div class="task"></div>
  </div>
</section>
<div class="band" style="top:2199px"></div>

<!-- Lesson -->
<section class="screen" style="top:2286px">
  <div class="side">
    <div class="brand">StrideUp</div>
    <svg class="search" style="left:286px;color:#fff"><use href="#i-search"/></svg>
    <div class="user">Nora Whitfield</div>
    <p class="center" style="top:212px;font-size:10px">GET A PROMOTION</p>
    <svg style="position:absolute;left:174px;top:242px;width:74px;height:74px;color:#fff"><use href="#i-award"/></svg>
    <h2 class="center" style="top:340px;font-size:19px;font-weight:600">Learn about Career Conversations</h2>
    <p class="center" style="top:375px;font-size:9.5px;font-weight:700">By Jonas Reed &nbsp;|&nbsp; Senior Marketing Lead, Northwind Co.</p>
    <a class="btn lime" href="#" style="left:124px;top:411px;width:176px;height:41px">&gt;&nbsp; Mark as Completed</a>
    <a class="btn ghost" href="#" style="left:124px;top:460px;width:176px;height:41px">&gt;&nbsp; Back to the List</a>
  </div>
  <div class="video">
    <div class="shot" role="img" aria-label="Video still of colleagues talking in an office lounge">
      <svg class="play" viewBox="0 0 68 68"><circle cx="34" cy="34" r="31" fill="rgba(197,93,135,.25)" stroke="var(--rose)" stroke-width="4"/><path d="M27 21l20 13-20 13z" fill="var(--rose)"/></svg>
    </div>
  </div>
  <div class="body-copy">
    <p>Lorem ipsum dolor sit amet, consectetur adipiscing elit. Vivamus rhoncus vulputate sollicitudin. Ut commodo gravida orci vel mattis. Mauris vitae elit dui. Donec enim enim, euismod a felis ac, aliquam varius leo. Etiam pretium pharetra leo, vitae scelerisque est egestas convallis. Interdum et malesuada fames ac ante ipsum primis in faucibus. Vivamus vel egestas ex, et molestie enim. Pellentesque nec mollis libero, vel iaculis mauris. Nullam arcu est, condimentum vitae ornare ac, blandit in dui. Mauris blandit aliquet dolor.</p>
    <ul>
      <li style="margin-left:-14px;list-style:none">Lorem ipsum dolor sit amet, consectetur adipiscing elit.</li>
      <li>Vivamus rhoncus vulputate sollicitudin.</li>
      <li>Ut commodo gravida orci vel mattis.</li>
      <li>Mauris vitae elit dui. Donec enim enim, euismod a felis ac, aliquam varius leo.</li>
    </ul>
  </div>
</section>
<style>.body-copy li:first-child::before{content:""}.body-copy li:first-child{margin-left:0!important}</style>
</body>
</html>
```